Letterhead for Conveyancing Company

Use existing logo to create a letterhead for a conveyancing company. Must be able to be used in Microsoft Word. Easy to read and professional.
Contact information to be at the bottom.
Brightwater Conveyancing Pty Ltd
ACN 621 984 736PO Box 535 Campbelltown SA 5074
Mobile - 0461 739 285
Web address - www.brightwaterconveyancing.com.au

Requirements
Must have
• Logo and contact details.
• Simple and professional.

```html
<!DOCTYPE html>
<html lang="en">
<head>
<meta charset="utf-8">
<title>Brightwater Conveyancing Letterhead</title>
<link href="https://fonts.googleapis.com/css2?family=Didact+Gothic&family=Roboto:wght@400;500;700&display=swap" rel="stylesheet">
<style>
  :root {
    --backdrop: #e4e4e4;
    --paper: #fafafa;
    --brand-pink: #e6409a;
    --ink-grey: #555555;
    --ink-soft: #6b6b6b;
    --rule: #cfcfcf;
    --signature-blue: #3a63b0;
  }
  * { margin: 0; padding: 0; box-sizing: border-box; }
  html, body {
    width: 1024px;
    height: 1200px;
    overflow: hidden;
    background: var(--backdrop);
  }
  .letterhead {
    position: absolute;
    left: 92px;
    top: 10px;
    width: 840px;
    height: 1180px;
    background: var(--paper);
    color: var(--ink-grey);
    font-family: "Didact Gothic", "Century Gothic", sans-serif;
  }
  .brand {
    position: absolute;
    left: 60px;
    top: 100px;
    display: flex;
    align-items: center;
    gap: 12px;
  }
  .brand-square {
    width: 26px;
    height: 26px;
    background: var(--brand-pink);
  }
  .brand-name {
    font-family: "Roboto", sans-serif;
    font-weight: 700;
    font-size: 36px;
    letter-spacing: -0.5px;
    color: var(--brand-pink);
  }
  .company-details {
    position: absolute;
    left: 522px;
    top: 80px;
    padding-left: 18px;
    border-left: 1px solid var(--rule);
    font-family: "Roboto", sans-serif;
    font-size: 13px;
    line-height: 18px;
    color: var(--ink-soft);
    height: 92px;
  }
  .company-name { font-weight: 500; color: var(--ink-grey); }
  .company-phone {
    display: flex;
    align-items: center;
    gap: 8px;
    margin-top: 8px;
  }
  .company-phone svg { width: 12px; height: 12px; }
  .letter-body {
    position: absolute;
    left: 81px;
    top: 316px;
    width: 690px;
  }
  .salutation {
    font-size: 20px;
    margin-bottom: 30px;
  }
  .letter-body p {
    font-size: 12px;
    line-height: 15.8px;
    text-align: justify;
    margin-bottom: 15.8px;
  }
  .letter-body p.closing { margin-top: 32px; }
  .signature {
    display: block;
    width: 150px;
    height: 66px;
    margin-top: 38px;
    background: linear-gradient(90deg, rgba(58,99,176,0.15), rgba(58,99,176,0.28));
    border-radius: 4px;
  }
  .footer-web {
    position: absolute;
    left: 0;
    right: 0;
    top: 1120px;
    text-align: center;
    font-family: "Roboto", sans-serif;
    font-size: 13px;
    letter-spacing: 3.2px;
    color: var(--ink-soft);
  }
</style>
</head>
<body>
  <main class="letterhead">
    <header>
      <div class="brand">
        <span class="brand-square"></span>
        <span class="brand-name">Brightwater</span>
      </div>
      <address class="company-details" style="font-style:normal">
        <div class="company-name">Brightwater Conveyancing Pty Ltd</div>
        <div>PO Box 812 Glenhaven SA 5091</div>
        <div>ACN 738 215 409</div>
        <div class="company-phone">
          <svg viewBox="0 0 24 24" aria-hidden="true"><path fill="#e6409a" d="M6.6 10.8c1.4 2.8 3.8 5.1 6.6 6.6l2.2-2.2c.3-.3.7-.4 1-.2 1.1.4 2.3.6 3.6.6.6 0 1 .4 1 1V20c0 .6-.4 1-1 1C10.6 21 3 13.4 3 4c0-.6.4-1 1-1h3.5c.6 0 1 .4 1 1 0 1.3.2 2.5.6 3.6.1.3 0 .7-.2 1z"/></svg>
          <span>0461 739 285</span>
        </div>
      </address>
    </header>

    <section class="letter-body">
      <div class="salutation">Dear Mr. Carter,</div>
      <p>Lorem ipsum dolor sit amet, consectetur adipiscing elit. Donec orci purus, luctus vitae dignissim eu, iaculis sed purus. Vivamus faucibus, ipsum nec aliquet viverra, leo mauris condimentum ligula, sit amet sagittis enim ligula quis arcu. Nam egestas tortor id nisi porttitor mattis. In tortor ante, ultricies in suscipit a, tempus non massa. Vivamus et auctor mi. Fusce vel massa nulla. Phasellus nec eros mauris, et scelerisque orci.</p>
      <p>Donec malesuada orci vitae nulla accumsan porta a id massa. Quisque accumsan iaculis magna sit amet fringilla. Maecenas consequat, magna eget tincidunt semper, odio nibh rutrum mi, id feugiat ante nisi eu risus. Vestibulum nunc orci, rhoncus a placerat in, ultricies in mi. Cras mattis varius eros, vel fringilla nisi suscipit eget. Quisque scelerisque sagittis nulla at porttitor.</p>
      <p>Sed id augue vitae urna euismod commodo aliquet a quam. Pellentesque arcu velit, cursus et malesuada ut, consequat et diam. Nullam erat sem, rhoncus id ullamcorper vitae, rhoncus et arcu. In ultricies ultricies nulla, ut rutrum nisi iaculis at. Donec eu magna a metus ornare faucibus. Fusce aliquet faucibus ultricies. Morbi semper, est id tincidunt gravida, sem arcu adipiscing lacus, ac bibendum nulla leo eu purus. Quisque nec diam sed risus consectetur a ccumsan quis quis nibh. Vestibulum id purus lorem.</p>
      <p>It is a long established fact that a reader will be distracted by the readable content of a page when looking at its layout. The point of using Lorem Ipsum is that it has a more-or-less normal distribution of letters, as opposed to using 'Content here, content here', making it look like readable English. Many desktop publishing packages</p>
      <p class="closing">Sincerely,</p>
      <span class="signature" role="img" aria-label="Handwritten signature of Daniel Carter in blue ink"></span>
    </section>

    <footer class="footer-web">www.brightwaterconveyancing.com.au</footer>
  </main>
</body>
</html>
```